Looking for potential sellers

We help people buy and sell homes and are currently looking for potential home sellers. We offer low commissions, are the Local Colorado Springs and Falcon Experts, homes selling fast and at top dollar, Free expert pricing opinions and Consultations, over 9 years of experience, top rated Realtors creative and aggressive marketing strategies. Never merely own a house, THRIVE at Harborview. phone number 482-630-9157 web thriveatharborview.com

```html
<!DOCTYPE html>
<html lang="en">
<head>
<meta charset="utf-8">
<title>Harborview Realty Postcard</title>
<link href="https://fonts.googleapis.com/css2?family=Open+Sans:wght@300;400;600;700&display=swap" rel="stylesheet">
<style>
  :root{
    --page:#e6e6e6;
    --ink:#1d1d1d;
    --olive:#9a9b2e;
    --olive-text:#a6a53a;
    --slate:rgba(90,90,90,.88);
    --white:#ffffff;
    --band-light:#e4e4e4;
    --mail:#222;
  }
  *{box-sizing:border-box;margin:0;padding:0}
  html,body{width:881px;height:1200px;overflow:hidden;background:var(--page);font-family:"Open Sans",Arial,sans-serif}
  .card{position:absolute;left:70px;width:740px;background:var(--ink);overflow:hidden}
  .front{top:59px;height:503px}
  .back{top:618px;height:500px;background:var(--white)}

  /* front */
  .hero-photo{position:absolute;left:0;top:0;width:740px;height:360px;
    background:linear-gradient(180deg,#7fb0dc 0%,#b9d3e8 22%,#e8e4da 45%,#d9d4c8 70%,#6f8f46 88%,#c9c9c2 100%)}
  .rule{position:absolute;left:0;height:6px;background:var(--olive)}
  .front .rule{top:360px;width:740px}
  .tag{position:absolute;left:0;height:74px;display:flex;align-items:center;padding-left:24px;color:var(--white);font-size:24px;white-space:nowrap}
  .tag-lead{top:78px;width:370px;background:var(--slate);font-weight:300}
  .tag-main{top:158px;width:330px;background:rgba(154,155,46,.92);font-weight:700}
  .agent-photo{position:absolute;background:linear-gradient(180deg,#c7895a 0%,#b06a45 35%,#5f6f86 65%,#3a4352 100%)}
  .front .agent-photo{left:0;top:315px;width:138px;height:188px}
  .brand{position:absolute;left:158px;top:400px;display:flex;align-items:center;gap:8px;color:var(--white);font-size:20px;font-weight:400}
  .brand-mark{width:12px;height:12px;background:var(--olive)}
  .agent-name{position:absolute;left:158px;top:472px;color:var(--olive-text);font-size:13.5px;font-weight:700;letter-spacing:.6px;white-space:nowrap}
  .pitch{position:absolute;left:363px;top:386px;width:360px;color:var(--white);font-size:12.2px;line-height:15px;text-align:justify}
  .contact{position:absolute;display:flex;align-items:center;gap:9px;color:var(--white);font-size:12.5px;letter-spacing:.3px;white-space:nowrap}
  .icon{width:17px;height:17px;flex:none}

  /* back */
  .panel{position:absolute;left:0;top:0;width:381px;height:500px;background:var(--ink)}
  .scene-photo{position:absolute;left:33px;top:22px;width:316px;height:158px;border:3px solid var(--olive);
    background:linear-gradient(180deg,#9fa3a8 0%,#8f7f76 30%,#bfc3c6 50%,#3e5a35 75%,#8d8a7a 100%)}
  .back-lead{position:absolute;left:28px;top:193px;color:var(--olive-text);font-size:18px;font-weight:300}
  .back-main{position:absolute;left:28px;top:215px;color:var(--white);font-size:18px;font-weight:700}
  .perks{position:absolute;left:30px;top:244px;list-style:none}
  .perks li{display:flex;align-items:center;gap:9px;height:19px;color:var(--white);font-size:12px}
  .perks svg{width:12px;height:12px;flex:none}
  .back .rule{top:413px;width:381px}
  .footer{position:absolute;left:0;top:419px;width:381px;height:81px;background:var(--band-light)}
  .back .agent-photo{left:0;top:388px;width:84px;height:112px;background:linear-gradient(180deg,#c98a66 0%,#b77a5a 40%,#3b3f48 70%,#2a2d33 100%)}
  .footer-name{position:absolute;left:106px;top:428px;color:var(--ink);font-size:13px;font-weight:700;letter-spacing:.4px;white-space:nowrap}
  .back .contact{color:var(--ink);font-size:12px;gap:7px;letter-spacing:.3px}
  .badge{position:absolute;left:328px;top:442px;width:38px;height:48px;background:var(--ink)}
  .indicia{position:absolute;left:639px;top:24px;width:78px;height:77px;border:1px solid var(--mail);
    font-family:Arial,sans-serif;font-size:11px;line-height:12.6px;text-align:center;padding-top:6px;color:var(--mail)}
  .indicia b{font-weight:700}
  .address{position:absolute;left:508px;top:138px;width:208px;height:83px;border:1px solid var(--mail);font-family:Arial,sans-serif;color:var(--mail)}
  .address .route{position:absolute;right:16px;top:10px;font-size:10px}
  .address .recipient{position:absolute;left:15px;top:40px;font-size:13px;line-height:14px}
</style>
</head>
<body>

<section class="card front">
  <div class="hero-photo" role="img" aria-label="Two-storey stucco home with garage under blue sky"></div>
  <div class="tag tag-lead">Never Merely Own a House.</div>
  <div class="tag tag-main">THRIVE at Harborview.</div>
  <div class="rule"></div>
  <div class="agent-photo" role="img" aria-label="Portrait of agent Dylan Mercer"></div>
  <div class="brand"><span class="brand-mark"></span>Keystone Realty</div>
  <div class="agent-name">Dylan Mercer, REALTOR®</div>
  <p class="pitch">We know that buying or selling your home can be one of the most exciting (and sometimes trying) times of your life. Because of this, we make a concerted effort to know and understand your wants and needs, which plays a crucial part in both your success, and ours.</p>
  <div class="contact" style="left:363px;top:474px">
    <svg class="icon" viewBox="0 0 20 20"><circle cx="10" cy="10" r="10" fill="#9a9b2e"/><circle cx="10" cy="10" r="5.5" fill="none" stroke="#1d1d1d" stroke-width="1.4"/><path d="M4.5 10h11M10 4.5c-3 3.5-3 7.5 0 11M10 4.5c3 3.5 3 7.5 0 11" fill="none" stroke="#1d1d1d" stroke-width="1.2"/></svg>
    www.thriveatharborview.com
  </div>
  <div class="contact" style="left:610px;top:474px">
    <svg class="icon" viewBox="0 0 20 20"><circle cx="10" cy="10" r="10" fill="#9a9b2e"/><path d="M7 5.5l2 2-1.2 1.4c.7 1.5 1.8 2.6 3.3 3.3L12.5 11l2 2-1.4 1.6c-3.8-.5-7-3.7-7.6-7.6z" fill="#1d1d1d"/></svg>
    482-630-9157
  </div>
</section>

<section class="card back">
  <div class="panel"></div>
  <div class="scene-photo" role="img" aria-label="Neighbourhood homes below mountain foothills"></div>
  <div class="back-lead">Never Merely Own a House.</div>
  <div class="back-main">THRIVE at Harborview.</div>
  <ul class="perks">
    <li><svg viewBox="0 0 12 12"><circle cx="6" cy="6" r="5.3" fill="none" stroke="#9a9b2e" stroke-width="1.2"/><path d="M5 3.5L7.5 6 5 8.5" fill="none" stroke="#9a9b2e" stroke-width="1.4"/></svg>Low commissions</li>
    <li><svg viewBox="0 0 12 12"><circle cx="6" cy="6" r="5.3" fill="none" stroke="#9a9b2e" stroke-width="1.2"/><path d="M5 3.5L7.5 6 5 8.5" fill="none" stroke="#9a9b2e" stroke-width="1.4"/></svg>Local Colorado Springs and Falcon Experts</li>
    <li><svg viewBox="0 0 12 12"><circle cx="6" cy="6" r="5.3" fill="none" stroke="#9a9b2e" stroke-width="1.2"/><path d="M5 3.5L7.5 6 5 8.5" fill="none" stroke="#9a9b2e" stroke-width="1.4"/></svg>Homes selling fast and at top dollar</li>
    <li><svg viewBox="0 0 12 12"><circle cx="6" cy="6" r="5.3" fill="none" stroke="#9a9b2e" stroke-width="1.2"/><path d="M5 3.5L7.5 6 5 8.5" fill="none" stroke="#9a9b2e" stroke-width="1.4"/></svg>Free expert pricing opinions and Consultations</li>
    <li><svg viewBox="0 0 12 12"><circle cx="6" cy="6" r="5.3" fill="none" stroke="#9a9b2e" stroke-width="1.2"/><path d="M5 3.5L7.5 6 5 8.5" fill="none" stroke="#9a9b2e" stroke-width="1.4"/></svg>Over 9 years of experience</li>
    <li><svg viewBox="0 0 12 12"><circle cx="6" cy="6" r="5.3" fill="none" stroke="#9a9b2e" stroke-width="1.2"/><path d="M5 3.5L7.5 6 5 8.5" fill="none" stroke="#9a9b2e" stroke-width="1.4"/></svg>Top rated Realtors</li>
    <li><svg viewBox="0 0 12 12"><circle cx="6" cy="6" r="5.3" fill="none" stroke="#9a9b2e" stroke-width="1.2"/><path d="M5 3.5L7.5 6 5 8.5" fill="none" stroke="#9a9b2e" stroke-width="1.4"/></svg>Creative and aggressive marketing strategies</li>
  </ul>
  <div class="rule"></div>
  <div class="footer"></div>
  <div class="agent-photo" role="img" aria-label="Portrait of agent Grant Holloway"></div>
  <div class="footer-name">Grant Holloway, REALTOR®</div>
  <div class="contact" style="left:106px;top:451px">
    <svg class="icon" viewBox="0 0 20 20"><circle cx="10" cy="10" r="10" fill="#1d1d1d"/><path d="M7 5.5l2 2-1.2 1.4c.7 1.5 1.8 2.6 3.3 3.3L12.5 11l2 2-1.4 1.6c-3.8-.5-7-3.7-7.6-7.6z" fill="#fff"/></svg>
    482-630-9157
  </div>
  <div class="contact" style="left:106px;top:472px">
    <svg class="icon" viewBox="0 0 20 20"><circle cx="10" cy="10" r="10" fill="#1d1d1d"/><circle cx="10" cy="10" r="5.5" fill="none" stroke="#fff" stroke-width="1.4"/><path d="M4.5 10h11M10 4.5c-3 3.5-3 7.5 0 11M10 4.5c3 3.5 3 7.5 0 11" fill="none" stroke="#fff" stroke-width="1.2"/></svg>
    www.thriveatharborview.com
  </div>
  <div class="badge"></div>

  <div class="indicia">PRSRT STD<br>ECRWSS<br>U.S. Postage<br><b>PAID</b><br>EDDM RETAIL</div>
  <div class="address">
    <span class="route">****************ECRWSS****</span>
    <div class="recipient">Local<br>Postal Customer</div>
  </div>
</section>

</body>
</html>
```